BANNER FOR ONLINE CABINET COMPANY MAIN PAGE

Need 3 different banners for the main page. We are online platform for ordering cabinets, parts etc. online.
Website: trimfit.ca
A place where the banner will be placed: https://view.snapvault.example/qR7TpWzKmB4eX
Banner size: 1344x399 pixels
****Clients should get the main point that they can order everything online through the website.

Industry/Entity Type

online cabinets and parts ordering

Requirements
Must have
• online ordering icons, iphone, laptop, desktop pc - so clients get an idea that this is web based service to order cabinets

```html
<!DOCTYPE html>
<html lang="en">
<head>
<meta charset="utf-8">
<title>TrimFit – Order Online Banner</title>
<link rel="stylesheet" href="https://fonts.googleapis.com/css2?family=Roboto+Condensed:wght@300;700;800&display=swap">
<style>
  :root {
    --page-bg: #ffffff;
    --banner-pink: #f3aaa8;
    --banner-pink-light: #f6b7b4;
    --banner-pink-deep: #e8908e;
    --text-light: #ffffff;
    --badge-red: #e0463a;
    --badge-grey: #5f5a5a;
    --badge-grey-light: #a29c9c;
    --badge-text-edge: #222222;
    --device-black: #121212;
    --device-silver: #dedee2;
    --device-silver-dark: #a8a8ae;
    --kitchen-cabinet: #ecebe6;
    --kitchen-wall: #d9d6cf;
    --kitchen-counter: #4e4e50;
    --kitchen-wood: #c8925a;
    --kitchen-sage: #b9cdb8;
    --tile-light: #e3e8ef;
    --tile-mid: #bcc6d3;
    --phone-dark: #2c2c2c;
    --phone-light: #e9e7e2;
  }
  * { box-sizing: border-box; margin: 0; padding: 0; }
  html, body {
    width: 1200px; height: 462px; overflow: hidden;
    background: var(--page-bg);
    font-family: "Roboto Condensed", "Arial Narrow", sans-serif;
  }
  .canvas { position: relative; width: 1200px; height: 462px; }
  .banner {
    position: absolute; left: 66px; top: 72px; width: 1051px; height: 311px;
    overflow: hidden;
  }
  .banner-backdrop {
    position: absolute; inset: 0;
    background:
      radial-gradient(ellipse 260px 180px at 430px 130px, var(--banner-pink-light), transparent 70%),
      linear-gradient(180deg, var(--banner-pink) 0%, var(--banner-pink) 70%, var(--banner-pink-deep) 88%, var(--banner-pink) 100%);
  }
  .brand {
    position: absolute; left: 56px; top: 36px;
    display: flex; align-items: center; gap: 10px;
    color: var(--text-light); font-weight: 800; font-size: 46px; line-height: 1;
  }
  .brand-mark { width: 14px; height: 14px; background: var(--text-light); }
  .category-list {
    position: absolute; left: 52px; top: 118px; list-style: none;
    color: var(--text-light); font-weight: 300; font-size: 31px; letter-spacing: 0.6px;
    line-height: 42px;
  }
  .monitor { position: absolute; left: 647px; top: 26px; width: 320px; height: 260px; z-index: 1; }
  .tablet { position: absolute; left: 865px; top: 121px; width: 125px; height: 170px; z-index: 2; }
  .phone { position: absolute; left: 964px; top: 180px; width: 58px; height: 117px; z-index: 3; }
  .order-badge { position: absolute; left: 547px; top: 80px; width: 140px; height: 140px; z-index: 4; }
</style>
</head>
<body>
<div class="canvas">
  <section class="banner">
    <div class="banner-backdrop" role="img" aria-label="Softly washed pink photo of a bright modern kitchen with shelves, pendant lights and countertop appliances"></div>

    <div class="brand"><span class="brand-mark"></span><span class="brand-name">TrimFit</span></div>

    <ul class="category-list">
      <li>DECORATIVE HARDWARE</li>
      <li>KITCHEN ACCESSORIES</li>
      <li>VANITIES</li>
    </ul>

    <svg class="monitor" viewBox="0 0 320 260">
      <defs>
        <linearGradient id="monitorScreen" x1="0" y1="0" x2="0.35" y2="1">
          <stop offset="0%" stop-color="var(--kitchen-cabinet)"/>
          <stop offset="35%" stop-color="var(--kitchen-wall)"/>
          <stop offset="55%" stop-color="var(--kitchen-counter)"/>
          <stop offset="70%" stop-color="var(--kitchen-cabinet)"/>
          <stop offset="100%" stop-color="var(--kitchen-wood)"/>
        </linearGradient>
        <linearGradient id="monitorSide" x1="0" y1="0" x2="1" y2="0">
          <stop offset="0%" stop-color="transparent"/>
          <stop offset="100%" stop-color="var(--kitchen-sage)"/>
        </linearGradient>
      </defs>
      <rect x="0" y="0" width="320" height="220" rx="7" fill="var(--device-black)"/>
      <g role="img" aria-label="Photo of a white kitchen with grey countertop and wooden floor on the desktop screen">
        <rect x="12" y="11" width="296" height="170" fill="url(#monitorScreen)"/>
        <rect x="200" y="11" width="108" height="110" fill="url(#monitorSide)" opacity="0.8"/>
      </g>
      <path d="M0 189 H320 V212 Q320 220 312 220 H8 Q0 220 0 212 Z" fill="var(--device-silver)"/>
      <path d="M124 220 H196 L200 252 H120 Z" fill="var(--device-silver-dark)"/>
      <rect x="112" y="250" width="96" height="7" rx="3" fill="var(--device-silver)"/>
    </svg>

    <svg class="tablet" viewBox="0 0 125 170">
      <defs>
        <linearGradient id="tabletScreen" x1="0" y1="0" x2="0" y2="1">
          <stop offset="0%" stop-color="var(--tile-mid)"/>
          <stop offset="30%" stop-color="var(--tile-light)"/>
          <stop offset="65%" stop-color="var(--tile-mid)"/>
          <stop offset="88%" stop-color="var(--tile-light)"/>
          <stop offset="100%" stop-color="var(--kitchen-wood)"/>
        </linearGradient>
      </defs>
      <rect x="0" y="0" width="125" height="170" rx="9" fill="var(--device-black)"/>
      <rect x="6" y="7" width="113" height="156" rx="3" fill="url(#tabletScreen)" role="img" aria-label="Photo of a tiled kitchen wall with coffee machine and hanging utensils on the tablet screen"/>
    </svg>

    <svg class="phone" viewBox="0 0 58 117">
      <defs>
        <linearGradient id="phoneScreen" x1="0" y1="0" x2="0" y2="1">
          <stop offset="0%" stop-color="var(--phone-dark)"/>
          <stop offset="30%" stop-color="var(--phone-dark)"/>
          <stop offset="45%" stop-color="var(--phone-light)"/>
          <stop offset="85%" stop-color="var(--phone-light)"/>
          <stop offset="100%" stop-color="var(--phone-dark)"/>
        </linearGradient>
      </defs>
      <rect x="0" y="0" width="58" height="117" rx="9" fill="var(--device-black)"/>
      <rect x="4" y="4" width="50" height="109" rx="6" fill="url(#phoneScreen)" role="img" aria-label="Mobile storefront page showing a white shelf with decor on the phone screen"/>
    </svg>

    <svg class="order-badge" viewBox="0 0 140 140">
      <defs>
        <radialGradient id="badgeFill" cx="45%" cy="42%" r="62%">
          <stop offset="0%" stop-color="var(--badge-grey-light)"/>
          <stop offset="100%" stop-color="var(--badge-grey)"/>
        </radialGradient>
      </defs>
      <polygon points="128,70 118.3,82.9 120.2,99 105.4,105.4 99,120.2 82.9,118.3 70,128 57.1,118.3 41,120.2 34.6,105.4 19.8,99 21.7,82.9 12,70 21.7,57.1 19.8,41 34.6,34.6 41,19.8 57.1,21.7 70,12 82.9,21.7 99,19.8 105.4,34.6 120.2,41 118.3,57.1"
        fill="var(--badge-red)" stroke="var(--badge-red)" stroke-width="12" stroke-linejoin="round"/>
      <polygon points="128,70 118.3,82.9 120.2,99 105.4,105.4 99,120.2 82.9,118.3 70,128 57.1,118.3 41,120.2 34.6,105.4 19.8,99 21.7,82.9 12,70 21.7,57.1 19.8,41 34.6,34.6 41,19.8 57.1,21.7 70,12 82.9,21.7 99,19.8 105.4,34.6 120.2,41 118.3,57.1"
        fill="url(#badgeFill)" stroke="url(#badgeFill)" stroke-width="7" stroke-linejoin="round"/>
      <text x="70" y="72" text-anchor="middle" font-family="Roboto Condensed, sans-serif" font-weight="700" font-size="37" fill="var(--text-light)" stroke="var(--badge-text-edge)" stroke-width="2" paint-order="stroke">ORDER</text>
      <text x="70" y="97" text-anchor="middle" font-family="Roboto Condensed, sans-serif" font-weight="800" font-size="22" letter-spacing="0.5" fill="var(--text-light)" stroke="var(--badge-text-edge)" stroke-width="2" paint-order="stroke">ONLINE</text>
    </svg>
  </section>
</div>
</body>
</html>
```